Flyer to Promote Membership in a Trade Association

UPDATE: I am looking for something modern and clean. NO CLIP ART. Not flashy. Just professional and modern. For everyone looking at our current flyer, we don't like it. That's why we aer looking for a new one. So please don't replicate it or use it as inspiration.

I need a flyer to promote membership in the Durable Residence Backers League. It can (probably should) be 2-sided. The content is attached as well as our logo and brand guidelines.

```html
<!DOCTYPE html>
<html lang="en">
<head>
<meta charset="utf-8">
<title>Durable Residence Backers League — Membership Flyer</title>
<link rel="stylesheet" href="https://fonts.googleapis.com/css2?family=Merriweather+Sans:wght@400;700;800&family=PT+Sans:wght@400;700&display=swap">
<style>
  :root{
    --orange:#ef8a3a;
    --orange-soft:#f3a567;
    --orange-line:#f2b27d;
    --charcoal:#4b4a4d;
    --ink:#3a3a3c;
    --muted:#6d6d70;
    --blue:#1f9fdc;
    --paper:#fbf6f1;
    --cream:#f6e6d8;
    --stage:#2d3846;
    --head:"Merriweather Sans", Arial, sans-serif;
    --body:"PT Sans", Arial, sans-serif;
  }
  *{box-sizing:border-box;margin:0;padding:0}
  html,body{width:1200px;height:900px;overflow:hidden}
  body{background:var(--stage);display:flex;align-items:center;justify-content:center;gap:24px;font-family:var(--body);color:var(--ink)}
  .page{position:relative;width:570px;height:738px;background:radial-gradient(circle at 70% 30%,var(--cream) 0,var(--paper) 55%);overflow:hidden}

  .brand{display:flex;align-items:center;gap:8px}
  .brand-mark{width:20px;height:20px;background:var(--orange);flex:none}
  .brand-name{font-family:var(--head);font-weight:700;font-size:13px;color:#7d838c;line-height:1.15;max-width:150px}

  /* ---------- benefits side ---------- */
  .benefits .brand{position:absolute;top:30px;left:300px}
  .tab{color:#fff;font-family:var(--head);font-weight:700;font-size:14px;padding:7px 16px 7px 28px}
  .tab-benefits{position:absolute;top:92px;left:0;background:var(--orange);width:230px}
  .col{position:absolute;display:flex;flex-direction:column;gap:8px;width:252px}
  .col-left{left:22px;top:134px}
  .col-right{left:296px;top:80px}
  .benefit{border:1px solid var(--orange-line);border-radius:14px;padding:9px 14px;background:rgba(255,255,255,.55)}
  .benefit h3{font-family:var(--head);font-weight:700;font-size:12.5px;color:var(--ink);margin-bottom:3px}
  .benefit p{font-size:11px;line-height:1.35;color:var(--muted)}
  .benefit.featured{background:var(--orange-soft);border-color:var(--orange-soft);padding:13px 16px}
  .benefit.featured h3,.benefit.featured p{color:#fff}
  .benefit .flag{display:block;font-family:var(--head);font-size:11px;font-weight:700;margin-bottom:5px;color:#fff}
  .members{position:absolute;left:0;right:0;bottom:76px}
  .tab-members{background:var(--charcoal);width:300px}
  .member-list{margin:10px 28px 0;font-size:10.5px;line-height:1.45;color:var(--ink)}
  .cta{position:absolute;left:0;right:0;bottom:0;height:60px;background:var(--blue);color:#fff;font-family:var(--head);font-weight:800;font-size:19px;display:flex;align-items:center;justify-content:center;gap:14px}

  /* ---------- front side ---------- */
  .front{display:flex;flex-direction:column;padding-top:30px}
  .front > *{margin-left:30px;margin-right:30px}
  .rule{height:1px;background:var(--orange-line);margin-top:14px}
  .headline{margin-top:14px}
  .headline h1{font-family:var(--head);font-weight:800;font-size:24px;color:var(--orange);line-height:1.2}
  .headline h2{font-family:var(--head);font-weight:400;font-size:15px;color:var(--charcoal);margin-top:6px}
  .intro{margin-top:8px;font-size:11.5px;line-height:1.45;color:var(--muted)}
  .front > .stats{margin:14px 0 0;height:72px;background:var(--charcoal);display:flex;justify-content:space-around;align-items:center;color:#fff}
  .stat{text-align:center}
  .stat strong{display:block;font-family:var(--head);font-weight:800;font-size:22px}
  .stat span{font-size:10.5px;letter-spacing:.06em;text-transform:uppercase}
  .front > .pillars{margin:16px 22px 0;display:flex;gap:8px}
  .pillar{flex:1;border:1px solid var(--orange-line);border-radius:12px;padding:12px 6px;text-align:center;background:rgba(255,255,255,.6)}
  .pillar-icon{display:block;margin:0 auto 8px;width:38px;height:38px}
  .pillar b{display:block;font-family:var(--head);font-size:11px;color:var(--orange);margin-bottom:3px}
  .pillar span{font-size:10.5px;color:var(--muted);line-height:1.25;display:block}
  .front > .promise{margin:18px 0 0;background:var(--orange);color:#fff;text-align:center;font-family:var(--head);font-weight:700;font-size:14px;line-height:1.4;padding:14px 40px}
  .join{margin-top:20px}
  .join h2{font-family:var(--head);font-weight:700;font-size:16px;color:var(--ink);margin-bottom:8px}
  .rates{width:100%;border-collapse:collapse;font-size:11px}
  .rates td{padding:9px 4px;border-top:1px solid var(--orange-line);vertical-align:top;color:var(--muted)}
  .rates td:first-child{font-family:var(--head);font-weight:700;color:var(--ink);width:130px;font-size:12px}
  .rates td:last-child{text-align:right;width:150px}
</style>
</head>
<body>

<section class="page benefits">
  <div class="brand"><span class="brand-mark"></span><span class="brand-name">Durable Residence Backers League</span></div>
  <div class="tab tab-benefits">Member Benefits</div>

  <div class="col col-left">
    <article class="benefit">
      <h3>Members-Only Conferences</h3>
      <p>Two annual in-person meetings. Spring Meeting: investors-only for candid peer conversations. Fall Summit: full ecosystem gathering with syndicators and brokers.</p>
    </article>
    <article class="benefit">
      <h3>Peer-to-Peer Meetups</h3>
      <p>Find your peers—underwriters, asset managers, credit officers and more—with our meetups.</p>
    </article>
    <article class="benefit featured">
      <h3>Shape Industry Standards</h3>
      <span class="flag">[INVESTOR ONLY]</span>
      <p>DRBL's underwriting and asset management standards are adopted industry-wide. Influence them through our committees.</p>
    </article>
  </div>

  <div class="col col-right">
    <article class="benefit">
      <h3>Investor-Only Forums</h3>
      <p>Exclusive meetings and webinars for investors only, enabling candid conversations and meaningful collaboration.</p>
    </article>
    <article class="benefit">
      <h3>Live &amp; On-Demand Webinars</h3>
      <p>Free monthly Third Thursday webinars covering Year 15 issues, secondary transactions, securitizing developer fees and other emerging topics.</p>
    </article>
    <article class="benefit">
      <h3>Searchable Member Directory</h3>
      <p>Find underwriters, asset managers, and credit officers—searchable by role, firm type, and investment approach.</p>
    </article>
    <article class="benefit featured">
      <h3>Emerging Leaders Program</h3>
      <span class="flag">[INVESTOR ONLY]</span>
      <p>Develop your firm's next-generation leaders through dedicated professional development programming.</p>
    </article>
  </div>

  <div class="members">
    <div class="tab tab-members">Our Investor Members Include</div>
    <p class="member-list">Harborline Life/Crestcare Health • Alder Bank • Summit Ridge National Bank • Bank of Meridia • Northfield Harbor Bank • Brightwater Financial • Keystone One • Pinecrest Bank • Lakeview Trust • Oakmont CDC • First Granite Bank • Willowmere Partners • Silverline Bank • Stonebridge Group • Countrywise Insurance • Hudson Crest Life • Tidewater (TRF) • Copperfield Real Estate • Riverbend Housing Finance • Bayshore Bank • Ironwood Coatings • Ashgrove Bank • Fairhaven Bank • Clearwater Community Capital • Redwood Valley Bank USA • Northstar Mutual • Evergate Impact Finance • Cedar Point Bank</p>
  </div>

  <div class="cta"><span>Ready to join?</span><span>drbl.org</span></div>
</section>

<section class="page front">
  <div class="brand"><span class="brand-mark"></span><span class="brand-name">Durable Residence Backers League</span></div>
  <div class="rule"></div>

  <header class="headline">
    <h1>Where LIHTC Investing Excellence Begins</h1>
    <h2>The Only Community Built Exclusively for Investors</h2>
  </header>
  <p class="intro">DRBL is where federal housing credit investors connect, learn, and lead. We are the only organization solely dedicated to LIHTC investors—giving you a trusted peer network, industry-setting standards, and the insights to stay informed.</p>

  <div class="stats">
    <div class="stat"><strong>30 YEARS</strong><span>Years of Impact</span></div>
    <div class="stat"><strong>60+</strong><span>Investor Firm</span></div>
    <div class="stat"><strong>1,000+</strong><span>Industry Professionals</span></div>
  </div>

  <div class="pillars">
    <div class="pillar">
      <svg class="pillar-icon" viewBox="0 0 38 38" role="img" aria-label="Icon for networking"><circle cx="19" cy="19" r="18" fill="#ececee"/></svg>
      <b>NETWORK</b><span>Peer Groups &amp; Forums</span>
    </div>
    <div class="pillar">
      <svg class="pillar-icon" viewBox="0 0 38 38" role="img" aria-label="Icon for learning"><circle cx="19" cy="19" r="18" fill="#ececee"/></svg>
      <b>LEARN</b><span>Conferences &amp; Webinars</span>
    </div>
    <div class="pillar">
      <svg class="pillar-icon" viewBox="0 0 38 38" role="img" aria-label="Icon for sharing"><circle cx="19" cy="19" r="18" fill="#ececee"/></svg>
      <b>SHARE</b><span>Candid Investor Exchange</span>
    </div>
    <div class="pillar">
      <svg class="pillar-icon" viewBox="0 0 38 38" role="img" aria-label="Icon for standards"><circle cx="19" cy="19" r="18" fill="#ececee"/></svg>
      <b>SHAPE</b><span>Standards &amp; Best Practices</span>
    </div>
    <div class="pillar">
      <svg class="pillar-icon" viewBox="0 0 38 38" aria-hidden="true"><rect x="6" y="24" width="5" height="8" fill="none" stroke="#4b4a4d" stroke-width="1.5"/><rect x="14" y="19" width="5" height="13" fill="none" stroke="#4b4a4d" stroke-width="1.5"/><rect x="22" y="14" width="5" height="18" fill="none" stroke="#4b4a4d" stroke-width="1.5"/><path d="M6 18 L16 11 L22 13 L32 5" fill="none" stroke="#4b4a4d" stroke-width="1.5"/><path d="M27 5 H32 V10" fill="none" stroke="#4b4a4d" stroke-width="1.5"/></svg>
      <b>GROW</b><span>Professional Development</span>
    </div>
  </div>

  <p class="promise">One membership, unlimited access. Your entire team can participate in DRBL activities.</p>

  <div class="join">
    <h2>Join DRBL Today</h2>
    <table class="rates">
      <tr><td>Investor Members</td><td>Banks, Insurance Companies, Economic Investors</td><td>$5,000/year (assets &gt;$5B)<br>$1,000/year (assets &lt;$5B)</td></tr>
      <tr><td>Affiliate Members</td><td>Syndicators &amp; Brokers</td><td>$4,500/year</td></tr>
    </table>
  </div>
</section>

</body>
</html>
```